Bref créative
Safety products company
Safety products for life
Professional
Gordon R Pike
President/Founder
482 Wexley Lane
Marlow Hollow, PA 16224-3871
866.41C.TOWN (412.8696)
pike@corvantahome.com
www.corvantahome.com
BE PREPARED
HOME
DISASTER
CHILD
SENIOR
PET
TRAVEL
BE PREPARED
the logo
"stacked" logo - two more will be coming with white backgrounds as soon as I receive them
4 AI LOGOS

```html
<!DOCTYPE html>
<html lang="en">
<head>
<meta charset="utf-8">
<title>Corvanta Home – Business Card</title>
<link rel="stylesheet" href="https://fonts.googleapis.com/css2?family=Open+Sans:wght@300;400;600&display=swap">
<style>
  :root{
    --canvas:#e9e4d8;
    --card-dark:#1f121b;
    --card-light:#ffffff;
    --accent:#e0381c;
    --accent-deep:#a8200e;
    --silver-hi:#e6e6e6;
    --silver-lo:#6d6d6d;
    --ink:#3a3a3a;
    --text-light:#f2f2f2;
    --divider:#9a8f95;
  }
  *{margin:0;padding:0;box-sizing:border-box}
  html,body{width:1200px;height:943px;overflow:hidden}
  body{background:var(--canvas);font-family:"Open Sans",Arial,sans-serif;position:relative}

  .card{position:absolute;left:300px;width:604px;height:352px;overflow:hidden;
        box-shadow:0 6px 14px rgba(0,0,0,.35)}
  .card-front{top:110px;background:var(--card-dark)}
  .card-back{top:493px;background:var(--card-light)}

  .edge-strip{position:absolute;left:0;top:0;width:13px;height:100%;
    background:linear-gradient(180deg,var(--silver-hi) 0%,var(--silver-lo) 50%,var(--accent-deep) 66%,var(--accent) 82%,#5a1108 100%)}
  .card-back .edge-strip{background:linear-gradient(180deg,var(--silver-hi) 0%,var(--silver-lo) 44%,#2a2a2a 50%,var(--accent) 56%,var(--accent-deep) 100%)}

  .brand{display:flex;align-items:center;gap:12px;color:var(--text-light);
    font-weight:600;letter-spacing:2px;text-transform:uppercase;white-space:nowrap}
  .brand-mark{width:22px;height:22px;background:var(--accent);flex:none}

  .front-brand{position:absolute;left:0;right:0;top:96px;justify-content:center;font-size:24px}
  .front-nav{position:absolute;left:13px;right:0;top:244px;text-align:center;white-space:nowrap;
    color:var(--text-light);font-size:14px;letter-spacing:.3px}
  .front-nav span + span::before{content:"|";margin:0 6px;color:var(--divider)}
  .front-url{position:absolute;left:13px;right:0;top:295px;text-align:center;
    color:var(--accent);font-size:14px;letter-spacing:1.5px}

  .back-top{position:absolute;left:0;top:0;width:100%;height:182px;background:var(--card-dark)}
  .back-brand{position:absolute;left:70px;top:102px;font-size:30px}
  .holder{position:absolute;left:324px;top:36px;color:var(--text-light);white-space:nowrap}
  .holder-name{font-size:19px;font-weight:400;letter-spacing:.5px;text-transform:uppercase;line-height:24px}
  .holder-title{font-size:13px;font-weight:300;line-height:18px}

  .address{position:absolute;right:326px;top:222px;text-align:right;color:var(--ink);
    font-size:13.5px;line-height:26px;white-space:nowrap}
  .contacts{position:absolute;left:336px;top:206px;list-style:none;color:var(--ink);font-size:13.5px;white-space:nowrap}
  .contacts li{display:flex;align-items:center;gap:12px;height:21px}
  .contacts svg{width:13px;height:13px;flex:none}
</style>
</head>
<body>

<section class="card card-front" aria-label="Card front">
  <div class="edge-strip"></div>
  <div class="brand front-brand"><span class="brand-mark"></span>Corvanta Home</div>
  <nav class="front-nav">
    <span>HOME</span><span>DISASTER</span><span>CHILD</span><span>SENIOR</span><span>PET</span><span>TRAVEL</span><span>BE PREPARED</span>
  </nav>
  <div class="front-url">www.corvantahome.com</div>
</section>

<section class="card card-back" aria-label="Card back">
  <div class="back-top"></div>
  <div class="edge-strip"></div>
  <div class="brand back-brand"><span class="brand-mark"></span>Corvanta Home</div>
  <div class="holder">
    <div class="holder-name">Gordon R Pike</div>
    <div class="holder-title">President/Founder</div>
  </div>
  <div class="address">
    <div>482 Wexley Lane</div>
    <div>Marlow Hollow, PA 16224-3871</div>
  </div>
  <ul class="contacts">
    <li><svg viewBox="0 0 12 12"><circle cx="6" cy="6" r="6" fill="#e0381c"/><path d="M4 3.2l1.2 1.5-.6.8c.4.9 1 1.5 1.9 1.9l.8-.6 1.5 1.2-.8 1.1C5.8 9 3 6.2 2.9 4z" fill="#fff"/></svg>866.41C.TOWN</li>
    <li><svg viewBox="0 0 12 12"><circle cx="6" cy="6" r="6" fill="#e0381c"/><path d="M4 3.2l1.2 1.5-.6.8c.4.9 1 1.5 1.9 1.9l.8-.6 1.5 1.2-.8 1.1C5.8 9 3 6.2 2.9 4z" fill="#fff"/></svg>8664128696</li>
    <li><svg viewBox="0 0 12 12"><rect x="3" y="0.5" width="6" height="11" rx="1.2" fill="#e0381c"/><rect x="4" y="2" width="4" height="6" fill="#fff"/></svg>814.362.5047</li>
    <li><svg viewBox="0 0 12 12"><rect x="0.5" y="2" width="11" height="7" fill="#e0381c"/><rect x="3" y="9" width="6" height="1.5" fill="#e0381c"/></svg>8142795630</li>
    <li><svg viewBox="0 0 12 12"><rect x="0.5" y="2.5" width="11" height="7" fill="#e0381c"/><path d="M1 3l5 3.5L11 3" stroke="#fff" fill="none"/></svg>pike@corvantahome.com</li>
  </ul>
</section>

</body>
</html>
```